Healthy Meal Delivery Website needs a new face lift

Hi there,

The current website i have is super old and outdated.

I would like a beautiful modern site that has all the same content as the previous except with a a new, modern and trustworthy feel.

The current website is http://www.plateorbit.ca/

Target Market(s)

Diet Meal delivery, weight loss, healthy meal delivery

Industry/Entity Type

Food Service

Number of Pages Required

5+ page

Font styles to use
Sans Serif

Requirements
Must have
• Modern & Clean
Should not have
• Anything outdated or cheesy

```html
<!DOCTYPE html>
<html lang="en">
<head>
<meta charset="utf-8">
<title>Plate Orbit Delivery – Fresh Diet Meals</title>
<link href="https://fonts.googleapis.com/css2?family=Cinzel:wght@400;700&family=Raleway:wght@400;500;600;700&display=swap" rel="stylesheet">
<style>
:root{
  --cyan:#29b6e0;
  --cyan-dark:#1ea6d3;
  --cyan-soft:#3fc1e8;
  --green:#8dc63f;
  --ink:#2b2b2b;
  --text:#555;
  --muted:#888;
  --page:#f2f2f2;
  --white:#fff;
  --line:#e3e3e3;
}
*{box-sizing:border-box;margin:0;padding:0}
html,body{width:1200px;height:4286px;overflow:hidden}
body{font-family:"Raleway",Arial,sans-serif;color:var(--text);background:var(--page);font-size:15px;line-height:1.55}
.display{font-family:"Cinzel",Georgia,serif;font-weight:400;color:var(--ink);text-align:center;letter-spacing:1px}
.photo{display:block}
.btn{display:inline-block;background:var(--green);color:#fff;font-weight:600;font-size:13px;padding:9px 20px;text-transform:uppercase}

/* header */
.site-header{height:150px;background:var(--white);border-top:7px solid var(--cyan);position:relative}
.brand{position:absolute;left:100px;top:26px;display:flex;align-items:center;gap:12px}
.brand-dot{width:18px;height:18px;border-radius:50%;background:var(--cyan)}
.brand-name{font-family:"Raleway",sans-serif;font-weight:700;font-size:30px;color:var(--cyan);line-height:1.05}
.tagline{position:absolute;left:350px;width:500px;top:40px;text-align:center;font-family:"Cinzel",serif;color:var(--cyan);font-size:19px;line-height:1.35;white-space:nowrap}
.tagline span{display:block;color:var(--ink);font-size:19px}
.contact-mini{position:absolute;right:100px;top:40px;width:140px}
.phone{display:flex;align-items:center;gap:8px;font-size:14px;color:var(--ink)}
.socials{display:flex;gap:7px;margin-top:10px}
.socials i{width:22px;height:22px;border-radius:50%;background:#222;display:block}
.socials i:last-child{background:var(--cyan)}
.main-nav{height:44px;background:var(--white);border-top:1px solid var(--line);border-bottom:1px solid var(--line);display:flex;align-items:center;padding-left:100px;font-size:12px;font-weight:600;color:#444;text-transform:uppercase}
.main-nav a{padding:0 16px;border-right:1px solid #ccc;line-height:14px}
.main-nav a.active{background:var(--cyan);color:#fff;line-height:44px;border:0}
.main-nav a.signup{background:var(--green);color:#fff;line-height:44px;border:0}

/* hero */
.hero{height:500px;position:relative;background:linear-gradient(160deg,#c9a478 0%,#9b6d3e 35%,#5e8a3a 65%,#3d6b2b 100%)}
.hero-caption{position:absolute;left:100px;top:206px;width:530px;height:86px;background:rgba(0,0,0,.45);padding:12px 20px}
.hero-caption h1{font-family:"Cinzel",serif;font-weight:400;color:#fff;font-size:34px;line-height:1.1}
.hero-caption p{color:#fff;font-size:16px}
.hero-arrow{position:absolute;left:22px;top:230px}

/* sample menu */
.sample{height:734px;padding-top:56px}
.sample h2{font-size:40px}
.sample-grid{display:flex;gap:28px;margin:30px 0 0 100px}
.sample-card{width:486px;height:506px;position:relative}
.sample-card .photo{height:420px}
.sample-info{position:absolute;left:40px;right:40px;top:340px;height:166px;background:#fff;text-align:center;padding:26px 30px}
.sample-info h3{font-size:22px;font-weight:600;color:var(--ink);margin-bottom:10px}
.sample-info p{font-size:13px}

/* feature */
.feature{height:472px;background:var(--white);position:relative}
.feature-copy{position:absolute;left:100px;top:40px;width:700px;font-size:13px;line-height:1.6}
.feature-copy h2{font-family:"Cinzel",serif;font-weight:400;font-size:21px;color:var(--cyan);margin-bottom:14px}
.feature-copy h2 b{color:var(--ink);font-weight:400}
.feature-copy .btn{margin-top:18px}
.feature .photo{position:absolute;left:814px;top:-8px;width:286px;height:480px;background:linear-gradient(180deg,#f4f4f4,#e2d7cf 60%,#cdbdb3)}

/* great tasting */
.tasting{height:388px;padding-top:44px}
.tasting h2{font-size:40px}
.tile-row{display:flex;gap:46px;margin:34px 0 0 100px}
.tile{width:303px;height:229px;position:relative}
.tile .photo{height:229px}
.tile-label{position:absolute;left:0;right:0;bottom:0;height:50px;background:var(--cyan-soft);color:#fff;font-weight:700;font-size:20px;text-align:center;line-height:50px;text-transform:uppercase}

/* program deals */
.deals{height:630px;padding-top:10px}
.deals h2{font-size:40px}
.deal-grid{display:grid;grid-template-columns:486px 486px;gap:36px 28px;margin:44px 0 0 100px}
.deal{height:229px;background:#fff;display:flex}
.deal .photo{width:171px;height:229px;flex:none}
.deal-body{padding:24px 22px;font-size:12.5px;line-height:1.5}
.deal-body h3{font-size:21px;font-weight:700;color:var(--ink);line-height:1.15;margin-bottom:10px;text-transform:uppercase}
.deal-body .btn{margin-top:10px;font-size:11px;padding:6px 14px}

/* team */
.team{height:234px;display:flex}
.team-badge{width:600px;background:var(--cyan-dark);position:relative}
.team-avatar{position:absolute;left:222px;top:26px;width:150px;height:150px;border-radius:50%;border:5px solid #fff;background:linear-gradient(180deg,#eee,#d9c8bc)}
.team-badge h2{position:absolute;left:0;right:0;bottom:18px;font-family:"Cinzel",serif;font-weight:400;color:#fff;font-size:36px;text-align:center}
.team-copy{flex:1;background:var(--cyan);color:#fff;font-size:13px;padding:64px 100px 0 80px}
.team-copy p+p{margin-top:18px}

/* testimonials */
.testimonials{height:480px;padding-top:44px;position:relative}
.testimonials h2{font-size:36px}
.quote-row{display:flex;gap:40px;margin:50px 0 0 190px}
.quote{width:248px;height:258px;background:#fff;position:relative;text-align:center;padding:56px 18px 0;font-size:13px}
.quote .mark{position:absolute;left:-4px;top:-18px;font-size:80px;color:var(--cyan);font-family:Georgia,serif;line-height:1}
.quote .avatar{position:absolute;left:94px;top:-30px;width:60px;height:60px;border-radius:50%;border:3px solid #fff;background:linear-gradient(180deg,#e9d6c4,#b98f72)}
.quote h4{font-size:14px;font-weight:700;color:var(--ink);margin-bottom:6px;white-space:nowrap}
.slider-arrow{position:absolute;top:267px;width:40px;height:40px;border-radius:50%;border:2px solid #777;display:flex;align-items:center;justify-content:center}

/* contact */
.contact{height:406px;background:radial-gradient(ellipse at 50% 70%,#5b4634 0%,#2e241d 55%,#1c1612 100%);padding-top:30px}
.contact h2{color:#fff;font-size:40px}
.contact-lede{color:#ddd;font-size:13px;text-align:center;margin-top:4px}
.contact-form{display:flex;gap:26px;margin:64px 0 0 157px}
.contact-form .message{width:430px;height:150px;background:#fff;padding:8px 12px;font-size:12px}
.fields{width:430px;display:flex;flex-direction:column;gap:12px}
.field{height:36px;background:#fff;padding:8px 12px;font-size:12px;color:var(--muted)}
.captcha{display:flex;gap:10px;align-items:center}
.captcha .field{width:230px}
.captcha .code{color:#fff;font-weight:700;font-size:14px;width:70px}
.captcha .submit{background:var(--cyan);color:#fff;font-weight:700;font-size:13px;height:36px;width:110px;text-align:center;line-height:36px}

/* footer */
.site-footer{height:143px;background:var(--page);position:relative;text-align:center;font-size:12px}
.to-top{position:absolute;left:574px;top:-26px;width:52px;height:52px;border-radius:50%;background:var(--cyan);display:flex;align-items:center;justify-content:center}
.site-footer p{padding-top:62px}
.site-footer p b{color:var(--ink)}
.site-footer .socials{justify-content:center;margin-top:10px}
</style>
</head>
<body>

<header class="site-header">
  <div class="brand"><span class="brand-dot"></span><div class="brand-name">Plate Orbit<br>Delivery Inc.</div></div>
  <div class="tagline">Fresh Customized Diet Meals Delivered Daily<span>Toronto and Canada Wide</span></div>
  <div class="contact-mini">
    <div class="phone">
      <svg width="14" height="14" viewBox="0 0 24 24"><path fill="#222" d="M6.6 10.8a15 15 0 0 0 6.6 6.6l2.2-2.2c.3-.3.7-.4 1-.2 1.1.4 2.3.6 3.6.6.6 0 1 .4 1 1V20c0 .6-.4 1-1 1A17 17 0 0 1 3 4c0-.6.4-1 1-1h3.5c.6 0 1 .4 1 1 0 1.3.2 2.5.6 3.6.1.3 0 .7-.2 1z"/></svg>
      416-555-0142
    </div>
    <div class="socials"><i></i><i></i><i></i><i></i></div>
  </div>
</header>

<nav class="main-nav">
  <a class="active">Home</a><a>How it works</a><a>Pricing</a><a>Sample menu</a><a>Celebrity</a><a>F.A.Q.</a><a>Contact</a><a class="signup">Sign up</a><a style="border:0">Customer login</a>
</nav>

<section class="hero" role="img" aria-label="Grilled chicken breast sliced over a fresh green salad">
  <svg class="hero-arrow" width="22" height="40" viewBox="0 0 22 40"><path d="M18 4 4 20l14 16" fill="none" stroke="#fff" stroke-width="4"/></svg>
  <div class="hero-caption">
    <h1>Fresh diet meals delivered</h1>
    <p>Providing Toronto diet meal delivery for 15 years</p>
  </div>
</section>

<section class="sample">
  <h2 class="display">Sample Menu - Plate Orbit Meals</h2>
  <div class="sample-grid">
    <article class="sample-card">
      <div class="photo" role="img" aria-label="Chef plating a dish with berries" style="background:linear-gradient(135deg,#f3f0ec,#e6ddd4 55%,#c9b7a6)"></div>
      <div class="sample-info"><h3>SAMPLE MENU #1</h3><p>At Plate Orbit Delivery, we have something for all tastes prepared with a focus on quality foods, nutritional balance and superior taste.</p></div>
    </article>
    <article class="sample-card">
      <div class="photo" role="img" aria-label="Roasted chicken pieces with dipping sauce" style="background:linear-gradient(135deg,#7a3d1e,#b2592b 50%,#5d2c14)"></div>
      <div class="sample-info"><h3>SAMPLE MENU #2</h3><p>We have made special considerations for both specific diet needs and allergies.</p></div>
    </article>
  </div>
</section>

<section class="feature">
  <div class="feature-copy">
    <h2>Fresh Diet Gourmet Meals Delivered <b>by Plate Orbit</b></h2>
    <p>Fresh diet meal delivery Toronto and Canada wide is our signature fresh gourmet diet meal delivery program designed for healthy living &amp; weight loss management. Diet meal delivery Toronto has a creative gourmet menu that uses exotic flavors and ingredients to enhance your dining experience.</p>
    <p>BENEFITS - Fresh diet meal delivery daily<br>MENU - Inspired fresh gourmet Orbit Diet meals<br>VARIETY - 60 Day Menu Rotation<br>CUSTOMIZATION - Every fresh Orbit Diet meal is personally customized<br>DELIVERY - Fresh diet meal delivery daily Toronto and Canada wide<br>CUSTOMER SERVICE - Personal Nutritionist available 7 days a week</p>
    <span class="btn">
      <svg width="12" height="11" viewBox="0 0 24 22" style="vertical-align:-1px;margin-right:6px"><path fill="#fff" d="M0 0h5l1 4h18l-3 10H8zM9 17a2.5 2.5 0 1 1 0 5 2.5 2.5 0 0 1 0-5zm10 0a2.5 2.5 0 1 1 0 5 2.5 2.5 0 0 1 0-5z"/></svg>Order now</span>
  </div>
  <div class="photo" role="img" aria-label="Smiling woman lifting a dumbbell"></div>
</section>

<section class="tasting">
  <h2 class="display">Great Tasting Diet Meal Delivery</h2>
  <div class="tile-row">
    <div class="tile"><div class="photo" role="img" aria-label="Fresh vegetables and fruit with a measuring tape" style="background:linear-gradient(135deg,#f6f6f6,#d9e8c4 45%,#e2563a 80%)"></div><div class="tile-label">Perfect diet</div></div>
    <div class="tile"><div class="photo" role="img" aria-label="Woman leaping in a sunny field" style="background:linear-gradient(180deg,#f7e3a3,#f0b25c 55%,#c6843c)"></div><div class="tile-label">Mindset</div></div>
    <div class="tile"><div class="photo" role="img" aria-label="Slim waist wrapped in a measuring tape" style="background:linear-gradient(180deg,#e8ecef,#d8c3b5 55%,#b9a293)"></div><div class="tile-label">Lose weight</div></div>
  </div>
</section>

<section class="deals">
  <h2 class="display">Program Deals</h2>
  <div class="deal-grid">
    <article class="deal">
      <div class="photo" role="img" aria-label="Woman enjoying a healthy meal" style="background:linear-gradient(180deg,#efe9e3,#c9b19d)"></div>
      <div class="deal-body"><h3>Customized for you</h3><p>The diet meal delivery program offers the widest selection of healthy options regarding your ingredients preference, allergies and special requests.</p><span class="btn">Order now</span></div>
    </article>
    <article class="deal">
      <div class="photo" role="img" aria-label="Wrap sandwiches with fresh filling" style="background:linear-gradient(180deg,#e4d2ae,#b8874f)"></div>
      <div class="deal-body"><h3>Pause your program anytime</h3><p>You are welcome to pause and restart your meal program at anytime. Our customers lead busy lives, therefore if you need to.</p><span class="btn">Order now</span></div>
    </article>
    <article class="deal">
      <div class="photo" role="img" aria-label="Roast dish with vegetables" style="background:linear-gradient(180deg,#a34a1e,#5a2a14)"></div>
      <div class="deal-body"><h3>Enjoy our gourmet menu</h3><p>Every fresh diet meal delivered is prepared with the finest ingredients available and has a creative menu that uses unique and exotic.</p><span class="btn">Order now</span></div>
    </article>
    <article class="deal">
      <div class="photo" role="img" aria-label="Colourful tacos on a dark table" style="background:linear-gradient(180deg,#3a2a22,#b5592d 50%,#2b211b)"></div>
      <div class="deal-body"><h3>Delivery system</h3><p>Learn about our delivery system. You will receive your full day's menu with a description of the meals, simple heating instructions and directions if the meal should.</p><span class="btn">Learn more</span></div>
    </article>
  </div>
</section>

<section class="team">
  <div class="team-badge">
    <div class="team-avatar" role="img" aria-label="Portrait of a team nutritionist"></div>
    <h2>The Plate Orbit Team</h2>
  </div>
  <div class="team-copy">
    <p>The Orbit Diet is based on 30% lean protein and the rest fruits and vegetables with a dash of Heart Healthy monounsaturated fats. Once these levels are reached and maintained, the body enters a state of hormonal balance which produces many positive effects, such as stable insulin and glucagon levels, increased energy, and weight loss.</p>
    <p>Made with love by PlateOrbit.ca</p>
  </div>
</section>

<section class="testimonials">
  <h2 class="display">Testimonials</h2>
  <div class="slider-arrow" style="left:116px"><svg width="12" height="16" viewBox="0 0 12 16"><path d="M9 2 3 8l6 6" fill="none" stroke="#666" stroke-width="2.5"/></svg></div>
  <div class="quote-row">
    <div class="quote"><span class="mark">&ldquo;</span><span class="avatar" role="img" aria-label="Customer portrait"></span><h4>Mara Ellison - Actress</h4><p>"The Orbit Diet is simple and it works! I am so grateful to have used the Orbit Diet. So tasty and so healthy."</p></div>
    <div class="quote"><span class="mark">&ldquo;</span><span class="avatar" role="img" aria-label="Customer portrait"></span><h4>Dane Korvik - Pro Hockey Player</h4><p>"I can train hard, eat well and feel great. Thank you PlateOrbit.ca for delivering such great food."</p></div>
    <div class="quote"><span class="mark">&ldquo;</span><span class="avatar" role="img" aria-label="Customer portrait"></span><h4>Lena Dufresne - Actress</h4><p>"I never used a prepared food service before but with my schedule on set Plate Orbit has been a blessing to me."</p></div>
  </div>
  <div class="slider-arrow" style="left:1044px"><svg width="12" height="16" viewBox="0 0 12 16"><path d="M3 2l6 6-6 6" fill="none" stroke="#666" stroke-width="2.5"/></svg></div>
</section>

<section class="contact" role="region" aria-label="Contact us, over a dimly lit plated meal">
  <h2 class="display">Contact Us</h2>
  <p class="contact-lede">Lorem Ipsum is simply dummy text of the printing and typesetting industry. Lorem Ipsum has been the industry's standard dummy text ever since the 1500s.</p>
  <div class="contact-form">
    <div class="message">Message</div>
    <div class="fields">
      <div class="field">Name</div>
      <div class="field">Email</div>
      <div class="captcha"><div class="field">Type the code shown</div><span class="code">MQB4I</span><span class="submit">SUBMIT</span></div>
    </div>
  </div>
</section>

<footer class="site-footer">
  <div class="to-top"><svg width="18" height="12" viewBox="0 0 18 12"><path d="M2 10 9 3l7 7" fill="none" stroke="#fff" stroke-width="3"/></svg></div>
  <p>Copyright © 2018 <b>Plate Orbit</b> . All Rights Reserved</p>
  <div class="socials"><i style="background:var(--cyan)"></i><i style="background:var(--cyan)"></i><i style="background:var(--cyan)"></i></div>
</footer>

</body>
</html>
```